Chatterly News Feed Advertisement for Bitcoin Startup

CoinHarbor is a bitcoin brokerage in South Africa.
We need an advertisement for our Chatterly newsfeed.
Modern, technology feel to the advertisement.
Colours should compliment our logo in the attached document
Advertisement text: "The cheapest Bitcoin in South Africa"
Creative hints: Include an image of a bitcoin. Include something visual relating to South Africa (map, flag etc.). These are just hints an do not need to be followed to the letter, we appreciate creative freedom.
Updates

Project Deadline Extended Reason: This advertisement will only be needed on 10th May. Added Monday, April 24, 2017

Target Market(s)

People wanting to purchase bitcoin

Industry/Entity Type

News

Font styles to use
Sans Serif

Colors

Designer to choose colors to be used in the design.

Requirements
Must have
• Size: 1000 x 561 pixels (landscape)
• Text must not constitute more than 20% of the design (as per Chatterly requirements0
Nice to have
• Attached is our logo for your reference. Creative freedom is yours.
Should not have
• No preferences

Files

```html
<!DOCTYPE html>
<html lang="en">
<head>
<meta charset="utf-8">
<title>The cheapest Bitcoin in South Africa – CoinHarbor</title>
<link href="https://fonts.googleapis.com/css2?family=Poppins:wght@600;700&display=swap" rel="stylesheet">
<style>
  :root {
    --navy: #1b2d55;
    --orange: #f7a823;
    --paper: #ffffff;
    --flag-red: #ee1c25;
    --flag-green: #00a651;
    --flag-yellow: #fff200;
    --flag-black: #000000;
    --flag-blue: #1174bf;
    --flag-white: #ffffff;
    --gold-light: #fbe07a;
    --gold-mid: #e8b02a;
    --gold-dark: #b9800f;
  }
  html, body {
    margin: 0;
    padding: 0;
    overflow: hidden;
    background: var(--paper);
  }
  .ad {
    position: relative;
    width: 1200px;
    height: 678px;
    overflow: hidden;
    background: var(--paper);
    font-family: "Poppins", sans-serif;
  }
  .flag-bands {
    position: absolute;
    inset: 0;
    width: 1200px;
    height: 678px;
  }
  .band-red { fill: var(--flag-red); }
  .band-white { fill: var(--flag-white); }
  .band-green { fill: var(--flag-green); }
  .band-yellow { fill: var(--flag-yellow); }
  .band-black { fill: var(--flag-black); }
  .band-blue { fill: var(--flag-blue); }

  .coin {
    position: absolute;
    left: 809px;
    top: 222px;
    width: 258px;
    height: 258px;
    border-radius: 50%;
    background: radial-gradient(circle at 40% 35%, var(--gold-light) 0%, var(--gold-mid) 55%, var(--gold-dark) 100%);
    box-shadow: 0 4px 10px rgba(0, 0, 0, 0.25);
  }

  .headline {
    margin: 0;
    position: absolute;
    left: 0;
    top: 0;
    font-weight: 700;
  }
  .headline span {
    position: absolute;
    left: 64px;
    white-space: nowrap;
    line-height: 1;
  }
  .headline-top {
    top: 117px;
    font-size: 88px;
    color: var(--navy);
    letter-spacing: -1px;
  }
  .headline-key {
    top: 200px;
    font-size: 140px;
    color: var(--orange);
    letter-spacing: -3px;
    text-shadow: 4px 5px 6px rgba(0, 0, 0, 0.35);
  }
  .headline-bottom {
    top: 358px;
    font-size: 88px;
    color: var(--navy);
    letter-spacing: -1px;
  }

  .brand {
    position: absolute;
    left: 248px;
    top: 506px;
    display: flex;
    align-items: center;
    gap: 12px;
  }
  .brand-mark {
    width: 36px;
    height: 44px;
    border-radius: 8px;
    background: var(--orange);
  }
  .brand-name {
    font-size: 30px;
    font-weight: 700;
    color: var(--navy);
    letter-spacing: -0.5px;
  }
</style>
</head>
<body>
  <main class="ad">
    <svg class="flag-bands" viewBox="0 0 1400 790" preserveAspectRatio="none" aria-hidden="true">
      <g class="bands-lower">
        <polygon class="band-red" points="635,790 790,790 1790,190 1635,190"/>
        <polygon class="band-white" points="790,790 830,790 1830,190 1790,190"/>
        <polygon class="band-green" points="830,790 935,790 1935,190 1830,190"/>
        <polygon class="band-yellow" points="935,790 985,790 1985,190 1935,190"/>
        <polygon class="band-black" points="985,790 1140,790 2140,190 1985,190"/>
        <polygon class="band-white" points="1140,790 1200,790 2200,190 2140,190"/>
        <polygon class="band-blue" points="1200,790 1400,790 2400,190 2200,190"/>
      </g>
      <g class="bands-upper">
        <polygon class="band-red" points="838,0 960,0 1960,1400 1838,1400"/>
        <polygon class="band-white" points="960,0 1005,0 2005,1400 1960,1400"/>
        <polygon class="band-green" points="1005,0 1095,0 2095,1400 2005,1400"/>
        <polygon class="band-yellow" points="1095,0 1140,0 2140,1400 2095,1400"/>
        <polygon class="band-black" points="1140,0 1275,0 2275,1400 2140,1400"/>
        <polygon class="band-white" points="1275,0 1290,0 2290,1400 2275,1400"/>
        <polygon class="band-blue" points="1290,0 1500,0 2500,1400 2290,1400"/>
      </g>
    </svg>

    <div class="coin" role="img" aria-label="Gold bitcoin coin illustration"></div>

    <h1 class="headline">
      <span class="headline-top">The cheapest</span>
      <span class="headline-key">BITCOIN</span>
      <span class="headline-bottom">in South Africa</span>
    </h1>

    <div class="brand">
      <span class="brand-mark" aria-hidden="true"></span>
      <span class="brand-name">CoinHarbor</span>
    </div>
  </main>
</body>
</html>
```